Hair and Wellness Brochure and Pricelist design

I am requiring a brochure that has a fresh, though alternative design. My business name is The Quiet Harbor Hair and Wellness. I have a very professional approach to my work and love to give that little bit extra to all of my clients. My passion for health, has led me to channel my business alternatively by using non toxic colours and styling products and through that same vein, I have studied Aromatherapy, Indian Head Massage and Reiki...all additional services I use where required.
My studio has very neutral tones of beige,white and beech wood but these tones aren't necessarily required for the brochure.I like to create a space of calm, peace and quiet, where my clients feel refreshed and rejuvenated..

```html
<!DOCTYPE html>
<html lang="en">
<head>
<meta charset="utf-8">
<title>The Quiet Harbor Hair and Wellness – Brochure</title>
<link rel="stylesheet" href="https://fonts.googleapis.com/css2?family=Kalam:wght@300;400&family=Tinos&display=swap">
<style>
  :root {
    --paper: #f6e9dc;
    --taupe: #a89b8c;
    --taupe-light: #ddd0c1;
    --rule: #cbbeb0;
    --ink-heading: #7d7064;
    --ink-body: #8e8174;
    --ink-soft: #a3968a;
    --white: #ffffff;
    --script: "Kalam", cursive;
    --serif: "Tinos", "Times New Roman", serif;
  }
  * { margin: 0; padding: 0; box-sizing: border-box; }
  html, body { width: 1200px; height: 900px; overflow: hidden; background: var(--paper); }
  .brochure { position: relative; width: 1200px; height: 900px; background: var(--paper); }
  .brochure > * { position: absolute; }

  .intro-title {
    left: 40px; top: 58px;
    font-family: var(--script); font-weight: 400; font-size: 52px; line-height: 1;
    color: var(--ink-heading);
  }
  .intro-rule { left: 20px; top: 158px; width: 361px; height: 7px; background: var(--rule); }
  .intro-text {
    left: 20px; top: 172px; width: 365px;
    font-family: var(--serif); font-size: 18px; line-height: 24.4px; color: var(--ink-body);
  }

  .note-title {
    left: 150px; top: 376px; width: 226px; text-align: right;
    font-family: var(--script); font-size: 30px; line-height: 1; color: var(--ink-heading);
  }
  .note-box { left: 24px; top: 402px; width: 357px; height: 296px; background: var(--taupe-light); z-index: -1; }
  .note-text {
    left: 46px; top: 424px; width: 320px;
    font-family: var(--script); font-weight: 300; font-size: 20.5px; line-height: 31px; color: var(--ink-body);
  }

  .placeholder {
    background: var(--taupe); color: var(--white);
    font-family: var(--serif); font-size: 22px; text-align: center;
  }
  .product-photos { left: 417px; top: 25px; width: 358px; height: 309px; padding-top: 112px; }
  .business-card { left: 806px; top: 15px; width: 379px; height: 230px; padding-top: 98px; font-size: 23px; letter-spacing: 0.5px; }

  .feature-text {
    left: 418px; top: 348px; width: 360px;
    font-family: var(--serif); font-size: 21.5px; line-height: 29.3px; color: var(--ink-body);
  }

  .callout {
    left: 46px; top: 718px; width: 709px; height: 147px; border-radius: 28px;
    background: var(--taupe); color: var(--white);
    padding: 20px 0 0 43px;
    font-family: var(--serif); font-size: 22px; line-height: 29px;
  }

  .tagline {
    left: 806px; top: 260px; width: 379px; text-align: center;
    font-family: var(--script); font-size: 30px; line-height: 37px; color: var(--taupe);
  }

  .spice-photo {
    left: 830px; top: 391px; width: 339px; height: 228px;
    background: linear-gradient(160deg, #7a4a2a 0%, #9b5f33 40%, #e0a02a 70%, #f3c35a 100%);
  }

  .service-list {
    left: 857px; top: 676px; list-style: none;
    font-family: var(--serif); font-size: 21px; line-height: 29px; color: var(--ink-soft);
  }
</style>
</head>
<body>
<main class="brochure">
  <h1 class="intro-title">Lorem Ipsum</h1>
  <div class="intro-rule"></div>
  <p class="intro-text">Lorem ipsum dolor sit amet, consectetur<br>adipiscing elit. Maecenas at ullamcorper<br>massa. Ut tellus risus, iaculis in velit non,<br>aliquet varius est. Nullam adipiscing con<br>sequat tortor, quis lacinia ipsum condime<br>ntum et. Nulla auctor aliquet consequat.<br>Fusce dictum dignissim nisl, mollis eleife<br>nd lorem iaculis et.</p>

  <div class="note-box"></div>
  <h2 class="note-title">Lorem Ipsum</h2>
  <p class="note-text">Lorem ipsum dolor sit amet,<br>consectetur adipiscing elit.<br>Maecenas at ullamcorper<br>massa. Ut tellus risus,<br>iaculis in velit non, aliquet<br>varius est. Nullam adipiscing<br>lorem ipsum dolor sit amet,<br>consectetur adipiscing elit..</p>

  <div class="placeholder product-photos">Photos hair products</div>

  <p class="feature-text">Lorem ipsum dolor sit amet, conse<br>ctetur adipiscing elit. Maecenas at<br>ullamcorper massa. Ut tellus risus,<br>iaculis in velit non, aliquet varius<br>est. Nullam adipiscing consequat<br>tortor, quis lacinia ipsum condime<br>Lorem ipsum dolor sit amet, conse<br>ctetur adipiscing elit. Maecenas at<br>ullamcorper massa. Ut tellus risus,<br>iaculis in velit non, aliquet varius<br>est. Nullam adipiscing consequat<br>tortor, quis lacinia ipsum condime.</p>

  <p class="callout">Lorem ipsum dolor sit amet, consectetur adipiscing elit.<br>Maecenas at ullamcorper massa. Ut tellus risus, iaculis<br>in velit non, aliquet varius est. Nullam adipiscing consequat<br>tortor, quis lacinia ipsum condimentum et.</p>

  <div class="placeholder business-card">business card</div>

  <p class="tagline">The Quiet Harbor<br>Hair and Wellness</p>

  <div class="spice-photo" role="img" aria-label="Photo of cinnamon sticks on dried orange slices"></div>

  <ul class="service-list">
    <li>Lorem ipsum dolor sit amet</li>
    <li>Lorem ipsum dolor sit amet</li>
    <li>Lorem ipsum dolor sit amet</li>
    <li>Lorem ipsum dolor sit amet</li>
  </ul>
</main>
</body>
</html>
```